Cosmetic Clinic Looking For Sign Designs

We are looking for sign design ideas for the front of our building and a lawn sign for our cosmetic injection salon.
I have uploaded the front of our building for a mock up and size, lawn posts with size and a sign that uses the same dimensions.
We would like both signs to be black for the background.

Target Market(s)

Ages 18-75

Industry/Entity Type

Beauty

Requirements
Must have
• Services we offer:
• Cosmetic Injections
• Airbrush Spray Tanning
• Eyelash Growth Serum
• Skin Care Products & More
• Everything must be on a black background
• The lawn sign must have the address: 394 Fenwick and the building sign should have the phone number.
Should not have
• Nothing can light up (no LED)
• Both signs do not need the full address. Just 394 Fenwick and the phone number

```html
<!DOCTYPE html>
<html lang="en">
<head>
<meta charset="utf-8">
<title>Bright Bloom Salon – Lawn Sign</title>
<link href="https://fonts.googleapis.com/css2?family=Roboto+Condensed:wght@500&family=Roboto:wght@300;400;700&display=swap" rel="stylesheet">
<style>
  :root {
    --sign-black: #13161d;
    --brand-teal: #2596b4;
    --accent-pink: #ec1a78;
    --badge-violet: #7b82c4;
    --service-white: #f1f1f1;
  }
  html, body {
    margin: 0;
    padding: 0;
    overflow: hidden;
    background: var(--sign-black);
  }
  .lawn-sign {
    display: block;
    width: 1200px;
    height: 1125px;
    background: var(--sign-black);
  }
  .brand-badge { fill: var(--badge-violet); stroke: var(--accent-pink); stroke-width: 9; }
  .brand-name {
    font-family: "Roboto Condensed", "Arial Narrow", sans-serif;
    font-weight: 500;
    fill: var(--brand-teal);
  }
  .brand-name--main { font-size: 112px; }
  .brand-name--sub { font-size: 60px; letter-spacing: 3px; }
  .accent-rule { fill: var(--accent-pink); }
  .service-list {
    font-family: "Roboto", Arial, sans-serif;
    font-weight: 400;
    font-size: 60px;
    letter-spacing: 1px;
    fill: var(--service-white);
  }
  .street-address {
    font-family: "Roboto", Arial, sans-serif;
    font-weight: 700;
    font-size: 76px;
    fill: var(--brand-teal);
  }
</style>
</head>
<body>
<svg class="lawn-sign" viewBox="0 0 1200 1125" xmlns="http://www.w3.org/2000/svg" role="img" aria-label="Bright Bloom Salon lawn sign">
  <rect width="1200" height="1125" fill="var(--sign-black)"/>

  <!-- Brand mark -->
  <circle class="brand-badge" cx="600" cy="208" r="112"/>

  <!-- Brand name -->
  <text class="brand-name brand-name--main" x="600" y="431" text-anchor="middle">BRIGHT BLOOM</text>
  <path class="accent-rule" d="M298 477 L478 473 L478 481 Z"/>
  <text class="brand-name brand-name--sub" x="600" y="498" text-anchor="middle">SALON</text>
  <path class="accent-rule" d="M902 477 L722 473 L722 481 Z"/>

  <!-- Side accents -->
  <path class="accent-rule" d="M70 658 Q74 740 70 822 Q66 740 70 658 Z"/>
  <path class="accent-rule" d="M1130 658 Q1134 740 1130 822 Q1126 740 1130 658 Z"/>

  <!-- Services -->
  <g class="service-list" text-anchor="middle">
    <text x="600" y="630">COSMETIC INJECTIONS</text>
    <text x="600" y="716">AIRBRUSH SPRAY TANNING</text>
    <text x="600" y="800">EYELASH GROWTH SERUM</text>
    <text x="600" y="884">SKIN CARE PRODUCTS &amp; MORE</text>
  </g>

  <!-- Divider -->
  <path class="accent-rule" d="M298 960 Q600 954 906 960 Q600 966 298 960 Z"/>

  <!-- Address -->
  <text class="street-address" x="600" y="1065" text-anchor="middle">394 Fenwick Street</text>
</svg>
</body>
</html>
```